Modernise Business Card

Our company has been operating for 10 years. With the start of the new decade we are looking to refresh our business card design. We manufacture a range of industrial product shipping to customers internationally. A copy of our current card, both sides, is attached. We are looking for a mature professional appearance.

```html
<!DOCTYPE html>
<html lang="en">
<head>
<meta charset="utf-8">
<title>Korvane Business Card</title>
<link rel="stylesheet" href="https://fonts.googleapis.com/css2?family=Poppins:wght@400;500;700;800&display=swap">
<style>
  :root {
    --brand-blue: #05acd3;
    --rule-brown: #4b433c;
    --ink: #4a4a4a;
    --paper: #ffffff;
    --backdrop: #2b2b2d;
  }
  * { margin: 0; padding: 0; box-sizing: border-box; }
  html, body {
    width: 1200px; height: 960px; overflow: hidden;
    background: var(--backdrop);
    font-family: "Poppins", sans-serif;
  }
  .sheet {
    position: relative; width: 1200px; height: 960px;
  }
  .card {
    position: absolute; left: 250px; width: 700px; height: 400px;
    box-shadow: 0 10px 30px rgba(0,0,0,.45);
    overflow: hidden;
  }
  /* Front */
  .card--front {
    top: 50px; background: var(--brand-blue); color: var(--paper);
    display: flex; flex-direction: column; align-items: center; justify-content: center;
  }
  .front__name {
    display: flex; align-items: center; gap: 16px;
    font-weight: 800; font-size: 96px; line-height: 1; letter-spacing: -1px;
  }
  .front__name .mark {
    width: 40px; height: 40px; background: var(--paper);
  }
  .front__tagline {
    margin-top: 22px; font-weight: 700; font-size: 19px; letter-spacing: .2px;
  }
  /* Back */
  .card--back {
    top: 510px; background: var(--paper);
  }
  .back__rule {
    position: absolute; top: 62px; height: 6px; background: var(--rule-brown);
  }
  .back__rule--left { left: 0; width: 190px; }
  .back__rule--right { right: 0; width: 190px; }
  .back__person {
    position: absolute; top: 38px; left: 190px; width: 320px;
    text-align: center; color: var(--brand-blue);
    font-weight: 800; font-size: 38px; line-height: 54px; text-transform: uppercase;
    letter-spacing: .5px;
  }
  .back__details {
    position: absolute; top: 130px; left: 0; right: 0;
    display: flex; justify-content: center;
    font-size: 19px; line-height: 27px; color: var(--ink);
  }
  .back__address {
    text-align: right; padding-right: 22px; width: 300px;
  }
  .back__divider {
    width: 2px; background: var(--ink); align-self: stretch;
  }
  .back__contact {
    padding-left: 22px; width: 380px;
  }
  .back__contact .label { color: var(--brand-blue); }
  .back__brand {
    position: absolute; left: 56px; bottom: 48px;
    display: flex; align-items: center; gap: 14px;
    color: var(--brand-blue); font-weight: 800; font-size: 82px; line-height: 1;
    letter-spacing: -1px;
  }
  .back__brand .mark { width: 34px; height: 34px; background: var(--brand-blue); }
</style>
</head>
<body>
<main class="sheet">
  <section class="card card--front" aria-label="Card front">
    <div class="front__name"><span class="mark"></span>Korvane</div>
    <p class="front__tagline">Hydraulic Adapters • Hose Fittings • Quick Couplings</p>
  </section>

  <section class="card card--back" aria-label="Card back">
    <div class="back__rule back__rule--left"></div>
    <div class="back__rule back__rule--right"></div>
    <h1 class="back__person">Alan Brisco</h1>

    <div class="back__details">
      <address class="back__address" style="font-style:normal">
        1208-3, Lianhe Tower<br>
        77 Meilin Road<br>
        Harbour District<br>
        Eastport 300100 China
      </address>
      <div class="back__divider"></div>
      <div class="back__contact">
        <span class="label">China :</span> +86 130 5550 1472<br>
        <span class="label">Australia:</span> +61 400 555 218<br>
        abrisco@korvanefittings.com<br>
        www.korvanefittings.com
      </div>
    </div>

    <div class="back__brand"><span class="mark"></span>Korvane</div>
  </section>
</main>
</body>
</html>
```